Stationery Design
Business Card, Envelopes and letterhead
Professional
Dwight Halloway
Production Manager
4172 N. Wrenfield Rd.
Baton Rouge LA 70913
dwight@velmorpack.com
www.velmorpack.com
Please propose letterhead, business card and envelope design using the new logo just uploaded

```html
<!DOCTYPE html>
<html lang="en">
<head>
<meta charset="utf-8">
<title>VPK Stationery Set</title>
<link href="https://fonts.googleapis.com/css2?family=Arimo:wght@400;700&display=swap" rel="stylesheet">
<style>
  :root {
    --backdrop: #c9c9c9;
    --paper: #ffffff;
    --paper-edge: #dcdcdc;
    --brand-cyan: #22a9e1;
    --brand-navy: #17355f;
    --ink: #4a4a4a;
    --ink-soft: #7a7a7a;
  }
  * { margin: 0; padding: 0; box-sizing: border-box; }
  html, body { width: 1200px; height: 655px; overflow: hidden; background: var(--backdrop); }
  body { font-family: "Arimo", Arial, sans-serif; color: var(--ink); }
  .canvas { position: relative; width: 1200px; height: 655px; overflow: hidden; }

  .sheet { position: absolute; background: var(--paper); box-shadow: 0 1px 3px rgba(0,0,0,0.18); }

  .brand { position: absolute; display: flex; flex-direction: column; }
  .brand-row { display: flex; align-items: center; gap: 5px; }
  .brand-dot { border-radius: 50%; background: var(--brand-cyan); }
  .brand-name { font-weight: 700; color: var(--brand-navy); line-height: 1; letter-spacing: 1px; }
  .brand-tagline { font-weight: 700; color: var(--brand-navy); text-transform: uppercase; letter-spacing: 0.3px; margin-top: 2px; }

  .band { position: absolute; left: 0; right: 0; background: var(--brand-cyan); display: flex; align-items: center; }
  .band-url { color: #fff; font-weight: 700; }

  .address, .phones, .email, .person { position: absolute; line-height: 1.45; color: var(--ink); }
  .phones { display: grid; grid-template-columns: auto auto; column-gap: 6px; }
  .person-name, .person-role { color: var(--brand-cyan); }

  /* Business card */
  .card { left: 24px; top: 281px; width: 163px; height: 137px; }
  .card .brand { left: 10px; top: 14px; }
  .card .brand-dot { width: 9px; height: 9px; }
  .card .brand-name { font-size: 14px; }
  .card .brand-tagline { font-size: 3px; }
  .card .person { right: 10px; top: 16px; text-align: right; font-size: 4.5px; }
  .card .address { left: 10px; top: 80px; font-size: 4px; }
  .card .phones { right: 10px; top: 80px; font-size: 4px; }
  .card .band { bottom: 10px; height: 10px; padding-left: 10px; }
  .card .band-url { font-size: 5px; }

  /* Letterhead */
  .letterhead { left: 192px; top: 29px; width: 408px; height: 626px; }
  .letterhead .brand { left: 22px; top: 22px; }
  .letterhead .brand-dot { width: 14px; height: 14px; }
  .letterhead .brand-name { font-size: 24px; }
  .letterhead .brand-tagline { font-size: 4.5px; }
  .letterhead .email { right: 22px; top: 24px; font-size: 5.5px; }
  .letterhead .address { left: 22px; top: 565px; font-size: 5.5px; }
  .letterhead .phones { right: 22px; top: 555px; font-size: 5.5px; }
  .letterhead .band { top: 590px; height: 24px; padding-left: 22px; }
  .letterhead .band-url { font-size: 8px; }

  /* Envelope back */
  .envelope-back { left: 660px; top: 79px; width: 511px; height: 235px; }
  .envelope-back .flap { position: absolute; left: 0; top: 0; width: 100%; height: 100%; }
  .envelope-back .brand { left: 50%; top: 16px; transform: translateX(-50%); align-items: center; }
  .envelope-back .brand-dot { width: 13px; height: 13px; }
  .envelope-back .brand-name { font-size: 22px; }
  .envelope-back .brand-tagline { font-size: 4px; }

  /* Envelope front */
  .envelope-front { left: 660px; top: 336px; width: 511px; height: 283px; }
  .envelope-front .brand { left: 20px; top: 26px; }
  .envelope-front .brand-dot { width: 14px; height: 14px; }
  .envelope-front .brand-name { font-size: 24px; }
  .envelope-front .brand-tagline { font-size: 4.5px; }
  .envelope-front .email { right: 22px; top: 34px; font-size: 5.5px; }
  .envelope-front .address { left: 20px; top: 226px; font-size: 5.5px; }
  .envelope-front .phones { right: 22px; top: 208px; font-size: 5.5px; }
  .envelope-front .band { top: 245px; height: 26px; padding-left: 20px; }
  .envelope-front .band-url { font-size: 8px; }
</style>
</head>
<body>
<main class="canvas">

  <section class="sheet card" aria-label="Business card">
    <div class="brand">
      <div class="brand-row"><span class="brand-dot"></span><span class="brand-name">VPK</span></div>
      <span class="brand-tagline">Industrial Packaging Supply</span>
    </div>
    <div class="person">
      <div class="person-name">Dwight Halloway</div>
      <div class="person-role">Production Manager</div>
    </div>
    <div class="address">
      <div>4172 N. Wrenfield Rd.</div>
      <div>Baton Rouge LA 70913</div>
      <div>dwight@velmorpack.com</div>
    </div>
    <div class="phones">
      <span>Toll free</span><span>1-800 555 0147</span>
      <span>Phone</span><span>225 555 0183</span>
      <span>Fax</span><span>225 555 0191</span>
    </div>
    <div class="band"><span class="band-url">www.velmorpack.com</span></div>
  </section>

  <section class="sheet letterhead" aria-label="Letterhead">
    <div class="brand">
      <div class="brand-row"><span class="brand-dot"></span><span class="brand-name">VPK</span></div>
      <span class="brand-tagline">Industrial Packaging Supply</span>
    </div>
    <div class="email">dwight@velmorpack.com</div>
    <div class="address">
      <div>4172 N. Wrenfield Rd.</div>
      <div>Baton Rouge LA 70913</div>
    </div>
    <div class="phones">
      <span>Toll free</span><span>1-800 555 0147</span>
      <span>Phone</span><span>225 555 0183</span>
      <span>Fax</span><span>225 555 0191</span>
    </div>
    <div class="band"><span class="band-url">www.velmorpack.com</span></div>
  </section>

  <section class="sheet envelope-back" aria-label="Envelope back">
    <svg class="flap" viewBox="0 0 511 235" preserveAspectRatio="none" aria-hidden="true">
      <path d="M0 0 L190 62 Q255 78 320 62 L511 0" fill="none" stroke="#cfcfcf" stroke-width="1"/>
      <path d="M0 235 L175 120 Q255 100 336 120 L511 235" fill="none" stroke="#e2e2e2" stroke-width="1"/>
    </svg>
    <div class="brand">
      <div class="brand-row"><span class="brand-dot"></span><span class="brand-name">VPK</span></div>
      <span class="brand-tagline">Industrial Packaging Supply</span>
    </div>
  </section>

  <section class="sheet envelope-front" aria-label="Envelope front">
    <div class="brand">
      <div class="brand-row"><span class="brand-dot"></span><span class="brand-name">VPK</span></div>
      <span class="brand-tagline">Industrial Packaging Supply</span>
    </div>
    <div class="email">dwight@velmorpack.com</div>
    <div class="address">
      <div>4172 N. Wrenfield Rd.</div>
      <div>Baton Rouge LA 70913</div>
    </div>
    <div class="phones">
      <span>Toll free</span><span>1-800 555 0147</span>
      <span>Phone</span><span>225 555 0183</span>
      <span>Fax</span><span>225 555 0191</span>
    </div>
    <div class="band"><span class="band-url">www.velmorpack.com</span></div>
  </section>

</main>
</body>
</html>
```